Sign Advertisment for Condominium Development

I need a sign created that will be placed in front of a building that is being converted into a luxury condominium development.

The sign needs to say:

Two, Boutique Luxury Condominiums Delivering late 2015.

Luxury Finishes // Designer Kitchens and Bath // Each Unit over 2,000 Square Feet

Deeded Parking Included with Each Unit

To Learn More, Contact:

Loretta Pinwell or Morgan Tesh
(202) 555-0147
Loretta.Pinwell@nrg-example.com

I need a small disclaimer at the bottom stating:

These Condominium(s) have not been registered by the Office of Residential Property Oversight Bureau of Dwelling Registration Tenancy Transfer and Purchase Section. A Condominium Unit may be reserved on a non-binding reservation agreement, but no contract of sale or lease that is binding on the purchaser may be entered into prior to registration.

Target Market(s)

Young professionals seeking luxury condominium

Industry/Entity Type

Building

Font styles to use
Serif

Colors
00a88f
ffffff

```html
<!DOCTYPE html>
<html lang="en">
<head>
<meta charset="utf-8">
<title>Two Boutique Luxury Condominiums</title>
<link rel="stylesheet" href="https://fonts.googleapis.com/css2?family=Montserrat:wght@900&family=Oswald:wght@500;700&family=Tinos:wght@400;700&display=swap">
<style>
  :root {
    --teal: #00a88f;
    --white: #ffffff;
    --ink: #1a1a1a;
    --serif: "Tinos", "Times New Roman", serif;
    --condensed: "Oswald", "Arial Narrow", sans-serif;
    --heavy: "Montserrat", "Arial Black", sans-serif;
  }
  * { margin: 0; padding: 0; box-sizing: border-box; }
  html, body { width: 1200px; height: 800px; overflow: hidden; background: var(--white); }
  .sign { position: relative; width: 1200px; height: 800px; background: var(--white); color: var(--ink); overflow: hidden; }

  .headline-number {
    position: absolute; left: 22px; top: 2px;
    font-family: var(--heavy); font-weight: 900; font-size: 196px;
    line-height: 1; letter-spacing: -6px; color: var(--teal);
  }
  .headline-stack {
    position: absolute; left: 586px; top: 20px; width: 600px;
    font-family: var(--condensed); font-weight: 700; text-transform: uppercase;
    text-align: center; line-height: 1; white-space: nowrap;
  }
  .headline-stack .line { display: block; font-size: 50px; line-height: 50px; letter-spacing: 1px; }
  .headline-stack .band {
    display: block; margin: 4px 0; padding: 1px 0 3px;
    background: var(--teal); color: var(--white); font-size: 44px; line-height: 44px;
  }

  .rule { position: absolute; left: 0; width: 1200px; height: 5px; background: var(--teal); }
  .rule-top { top: 196px; }
  .rule-bottom { top: 272px; }

  .features {
    position: absolute; left: 0; top: 215px; width: 1200px; text-align: center;
    font-family: var(--serif); font-weight: 700; font-size: 30px; line-height: 40px;
    white-space: nowrap;
  }
  .features .accent { color: var(--teal); }

  .parking {
    position: absolute; left: 0; top: 298px; width: 1200px; text-align: center;
    font-family: var(--condensed); font-weight: 500; font-size: 44px;
    letter-spacing: 5px; color: var(--teal); text-transform: uppercase; line-height: 1;
    white-space: nowrap;
  }

  .contact-panel {
    position: absolute; left: 0; top: 362px; width: 1200px; height: 292px;
    background: var(--teal); color: var(--white); text-align: center;
    font-family: var(--serif); font-weight: 700;
  }
  .contact-panel .inset { position: absolute; left: 0; top: 8px; width: 100%; height: 2px; background: var(--white); opacity: 0.85; }
  .contact-panel .lead { padding-top: 40px; font-size: 36px; line-height: 44px; }
  .contact-panel .details { margin-top: 36px; font-size: 36px; line-height: 44px; }

  .disclaimer {
    position: absolute; left: 26px; top: 674px; width: 1150px;
    font-family: var(--serif); font-size: 21px; line-height: 28px; color: var(--ink);
  }
</style>
</head>
<body>
<main class="sign">
  <div class="headline-number">TWO</div>
  <div class="headline-stack">
    <span class="line">Boutique Luxury</span>
    <span class="band">Condominiums Delivering</span>
    <span class="line">Late 2015</span>
  </div>

  <div class="rule rule-top"></div>
  <p class="features">Luxury Finishes // <span class="accent">Designer Kitchens and Bath</span> // Each Unit over 2,000 Square Feet</p>
  <div class="rule rule-bottom"></div>

  <p class="parking">Deeded Parking Included With Each Unit</p>

  <section class="contact-panel">
    <div class="inset"></div>
    <p class="lead">To Learn More, Contact:</p>
    <p class="details">Loretta Pinwell or Morgan Tesh<br>(202) 555-0147<br>Loretta.Pinwell@nrg-example.com</p>
  </section>

  <p class="disclaimer">These Condominium(s) have not been registered by the Office of Residential Property Oversight Bureau of Dwelling Registration Tenancy Transfer and Purchase Section. A Condominium Unit may be reserved on a non-binding reservation agreement, but no contract of sale or lease that is binding on the purchaser may be entered into prior to registration.</p>
</main>
</body>
</html>
```